Flyer for Daycare

A Flyer for family group daycare
Specfs:
- One side english / Another Side spanish(the text for both sides is below)
- The flyer is for printing in 5" x 7" or 5.5" x 8.5"
- The address and phone number is the most important
Logo(see the attachment)
NYC Licensed
Children from 6 Weeks to 12 years old
Accepting All the Programs( BWD, OFT) and Private
CPR & First Aid Certified
Full Time, Part Time and After School
----------------------------------------------------------------------------
Provide Homework Assistance
Potty Training
Outdoor Activities
Nutritional Meals & Snack
Baby Wipes
Text in Spanish
Licencia por el estado de NY
Niños de 6 semanas a 12 años
Aceptando Todos los Programas (BWD, OFT) y Privado
Certificación en CPR y Primeros Auxilios
Tiempo completo, tiempo parcial y después de la escuela
----------------------------------------------------------------------------------------------
Actividades al aire libre
Asistencia con la tarea
Entrenamiento para ir al baño
Desayunos, Comidas y refrigerios nutricionales
Toallitas para bebé
382 E 514th ST
APT 4C
Bronx, NY, 10758
ig: @velomarkdaycare
555-318-7704
LAtin and Black, Bronx NY Area
Daycare service

```html
<!DOCTYPE html>
<html lang="en">
<head>
<meta charset="utf-8">
<title>Velomark Day Care Flyers</title>
<link href="https://fonts.googleapis.com/css2?family=Lilita+One&family=Patrick+Hand&family=Roboto:wght@700&display=swap" rel="stylesheet">
<style>
  :root{
    --bg:#a9a9a9;
    --paper:#f6f6f7;
    --purple:#7d168f;
    --red:#d3101b;
    --blue:#14319c;
    --orange:#f08a1c;
    --green:#2a9a12;
    --navy:#0a2a9c;
    --ink:#1e1e1e;
    --star:#f39a1e;
    --white:#ffffff;
    --cloud-line:#bfc3cc;
  }
  *{margin:0;padding:0;box-sizing:border-box}
  html,body{width:1200px;height:904px;overflow:hidden;background:var(--bg)}
  .canvas{position:relative;width:1200px;height:904px}
  .flyer{position:absolute;top:26px;width:550px;height:851px;overflow:hidden;
    background:linear-gradient(160deg,var(--white) 0%,var(--paper) 55%,#e9eaee 100%)}
  .flyer--en{left:40px}
  .flyer--es{left:610px}
  .hero-photo{position:absolute;left:0;top:0;width:550px;height:370px;
    background:linear-gradient(120deg,#cfe3ee 0%,#e9d9c7 35%,#f0c94a 60%,#d8e6d0 80%,#c7dbe7 100%)}
  .cloud-edge{position:absolute;left:0;top:330px;width:550px;height:80px}
  .kids-photo{position:absolute;left:0;top:625px;width:340px;height:226px;
    clip-path:polygon(0 0,270px 0,270px 48px,340px 110px,340px 100%,0 100%);
    background:linear-gradient(100deg,#e8e4df 0%,#d9c2a8 40%,#5e79a8 70%,#e0a24a 100%)}
  .contact-band{position:absolute;left:0;top:680px;width:550px;height:171px}
  .brand{position:absolute;display:flex;align-items:center;gap:10px;z-index:2}
  .brand__dot{width:26px;height:26px;border-radius:50%;background:var(--orange)}
  .brand__name{font-family:"Lilita One",sans-serif;color:var(--blue);font-size:34px;line-height:1}
  .flyer--en .brand{left:300px;top:410px}
  .flyer--es .brand{left:312px;top:400px}
  .facts{position:absolute;left:30px;font-family:"Lilita One",sans-serif;white-space:nowrap;z-index:2}
  .flyer--en .facts{top:400px;font-size:20px;line-height:22px}
  .flyer--en .facts p{margin-bottom:6px}
  .flyer--es .facts{top:399px;font-size:16px;line-height:19px}
  .flyer--es .facts p{margin-bottom:8px}
  .c-purple{color:var(--purple)} .c-red{color:var(--red)} .c-blue{color:var(--blue)}
  .c-orange{color:var(--orange)} .c-green{color:var(--green)}
  .services{position:absolute;list-style:none;font-family:"Patrick Hand",cursive;color:var(--ink);font-size:17px;line-height:18px;white-space:nowrap;z-index:2}
  .services li{position:relative;padding-left:17px;margin-bottom:7px}
  .services li::before{content:"★";position:absolute;left:0;top:0;color:var(--star);font-size:13px}
  .flyer--en .services{left:282px;top:545px}
  .flyer--es .services{left:295px;top:529px}
  .contact{position:absolute;left:340px;top:738px;list-style:none;font-family:"Roboto",sans-serif;font-weight:700;color:var(--white);font-size:14px;line-height:1.2;z-index:2}
  .contact li{display:flex;gap:6px;margin-bottom:9px}
  .contact svg{flex:none;width:17px;height:17px;margin-top:1px}
</style>
</head>
<body>
<main class="canvas">

  <section class="flyer flyer--en" lang="en">
    <div class="hero-photo" role="img" aria-label="Photo of a caregiver and three children stacking colourful wooden blocks at a table"></div>
    <svg class="cloud-edge" viewBox="0 0 550 80" aria-hidden="true">
      <path d="M0 80 L0 48 Q20 28 45 44 Q70 30 95 48 Q125 30 150 46 Q180 28 205 44 Q240 24 270 36 Q300 10 340 16 Q380 0 420 14 Q460 2 500 18 Q530 8 550 22 L550 80 Z" fill="#fafafa" stroke="var(--cloud-line)" stroke-width="3"/>
    </svg>
    <div class="kids-photo" role="img" aria-label="Photo of two smiling children holding toy rings up to their eyes"></div>
    <svg class="contact-band" viewBox="0 0 550 171" aria-hidden="true">
      <path d="M350 171 L257 30 Q275 10 300 24 Q325 4 350 20 Q380 2 410 18 Q440 0 470 14 Q500 -2 525 12 Q540 4 550 8 L550 171 Z" fill="var(--navy)" stroke="var(--cloud-line)" stroke-width="3"/>
    </svg>
    <div class="brand"><span class="brand__dot"></span><span class="brand__name">Velomark<br>Day Care</span></div>
    <div class="facts">
      <p class="c-purple">NYC Licensed</p>
      <p class="c-red">Children from 6 Weeks to<br>12 years old</p>
      <p class="c-blue">Accepting All the Programs<br>( BWD, OFT) and Private</p>
      <p class="c-orange">CPR &amp; First Aid Certified</p>
      <p class="c-green">Full Time, Part Time<br>&amp; After School</p>
    </div>
    <ul class="services">
      <li>Provide Homework Assistance</li>
      <li>Potty Training</li>
      <li>Outdoor Activities</li>
      <li>Nutritional Meals &amp; Snack</li>
      <li>Baby Wipes</li>
    </ul>
    <ul class="contact">
      <li><svg viewBox="0 0 20 20"><circle cx="10" cy="10" r="9" fill="none" stroke="#fff" stroke-width="1.6"/><path d="M10 4.5a3.5 3.5 0 0 0-3.5 3.5c0 2.6 3.5 6.5 3.5 6.5s3.5-3.9 3.5-6.5A3.5 3.5 0 0 0 10 4.5z" fill="#fff"/></svg><span>382 E 514th ST APT 4C,<br>Bronx, NY, 10758</span></li>
      <li><svg viewBox="0 0 20 20"><circle cx="10" cy="10" r="9" fill="none" stroke="#fff" stroke-width="1.6"/><path d="M6.5 5.5l2 0 1 2.5-1.3 1c.6 1.3 1.5 2.2 2.8 2.8l1-1.3 2.5 1v2c0 .5-.5 1-1 1C9 14.5 5.5 11 5.5 6.5c0-.5.5-1 1-1z" fill="#fff"/></svg><span>555-318-7704</span></li>
      <li><svg viewBox="0 0 20 20"><circle cx="10" cy="10" r="9" fill="none" stroke="#fff" stroke-width="1.6"/></svg><span>ig: @velomarkdaycare</span></li>
    </ul>
  </section>

  <section class="flyer flyer--es" lang="es">
    <div class="hero-photo" role="img" aria-label="Foto de una cuidadora y tres niños apilando bloques de madera de colores"></div>
    <svg class="cloud-edge" viewBox="0 0 550 80" aria-hidden="true">
      <path d="M0 80 L0 48 Q20 28 45 44 Q70 30 95 48 Q125 30 150 46 Q180 28 205 44 Q240 24 270 36 Q300 10 340 16 Q380 0 420 14 Q460 2 500 18 Q530 8 550 22 L550 80 Z" fill="#fafafa" stroke="var(--cloud-line)" stroke-width="3"/>
    </svg>
    <div class="kids-photo" role="img" aria-label="Foto de dos niños sonrientes sosteniendo aros de juguete frente a los ojos"></div>
    <svg class="contact-band" viewBox="0 0 550 171" aria-hidden="true">
      <path d="M350 171 L257 30 Q275 10 300 24 Q325 4 350 20 Q380 2 410 18 Q440 0 470 14 Q500 -2 525 12 Q540 4 550 8 L550 171 Z" fill="var(--navy)" stroke="var(--cloud-line)" stroke-width="3"/>
    </svg>
    <div class="brand"><span class="brand__dot"></span><span class="brand__name">Velomark<br>Day Care</span></div>
    <div class="facts">
      <p class="c-purple">Licencia por el estado de NY</p>
      <p class="c-red">Niños de 6 semanas a 12 años</p>
      <p class="c-blue">Aceptando Todos los<br>Programas (BWD, OFT) y Privado</p>
      <p class="c-orange">Certificación en CPR y Primeros<br>Auxilios</p>
      <p class="c-green">Tiempo completo, tiempo parcial<br>y después de la escuela</p>
    </div>
    <ul class="services">
      <li>Actividades al aire libre</li>
      <li>Asistencia con la tarea</li>
      <li>Entrenamiento para ir al baño</li>
      <li>Desayunos, Comidas y<br>refrigerios nutricionales</li>
      <li>Toallitas para bebé</li>
    </ul>
    <ul class="contact">
      <li><svg viewBox="0 0 20 20"><circle cx="10" cy="10" r="9" fill="none" stroke="#fff" stroke-width="1.6"/><path d="M10 4.5a3.5 3.5 0 0 0-3.5 3.5c0 2.6 3.5 6.5 3.5 6.5s3.5-3.9 3.5-6.5A3.5 3.5 0 0 0 10 4.5z" fill="#fff"/></svg><span>382 E 514th ST APT 4C,<br>Bronx, NY, 10758</span></li>
      <li><svg viewBox="0 0 20 20"><circle cx="10" cy="10" r="9" fill="none" stroke="#fff" stroke-width="1.6"/><path d="M6.5 5.5l2 0 1 2.5-1.3 1c.6 1.3 1.5 2.2 2.8 2.8l1-1.3 2.5 1v2c0 .5-.5 1-1 1C9 14.5 5.5 11 5.5 6.5c0-.5.5-1 1-1z" fill="#fff"/></svg><span>555-318-7704</span></li>
      <li><svg viewBox="0 0 20 20"><circle cx="10" cy="10" r="9" fill="none" stroke="#fff" stroke-width="1.6"/></svg><span>ig: @velomarkdaycare</span></li>
    </ul>
  </section>

</main>
</body>
</html>
```